Webbanner-Design für Beteiligungsunternehmen
Zielgruppe
Ich habe ein kleines Familieninternes Beteiligungsunternehmen welches an verschiedenen Firmen beteiligt ist.
Aufgabenstellung
Ich brauche ein Profilbanner für Facebook und Twitter welches zum einen meine Hauptmarke 'Mertlow Holding' und meine Unternehmen an denen ich beteiligt bin (Geldwacht/Kaldoran Real Estate/ TK Holding/Brivalo) zeigt.

```html
<!DOCTYPE html>
<html lang="de">
<head>
<meta charset="utf-8">
<title>Mertlow Holding – Profilbanner</title>
<link rel="stylesheet" href="https://fonts.googleapis.com/css2?family=Saira:wght@500&display=swap">
<style>
  :root {
    --page: #ffffff;
    --brick-red: #8a6a6c;
    --brick-rose: #9c7f80;
    --brick-grey: #9d918d;
    --mortar: #cbbfae;
    --band: rgba(140, 138, 138, 0.88);
    --mark: #ffffff;
    --shadow: rgba(0, 0, 0, 0.35);
  }
  * { margin: 0; padding: 0; box-sizing: border-box; }
  html, body {
    width: 1200px; height: 845px; overflow: hidden;
    background: var(--page);
    font-family: "Saira", "Arial", sans-serif;
    font-weight: 500;
  }
  .canvas { position: relative; width: 1200px; height: 845px; }

  .banner {
    position: absolute;
    overflow: hidden;
    box-shadow: 0 4px 14px var(--shadow);
  }
  .banner--small { left: 320px; top: 80px; width: 560px; height: 213px; }
  .banner--large { left: 88px; top: 423px; width: 1023px; height: 341px; }

  .wall-photo {
    position: absolute; inset: 0;
    background:
      radial-gradient(ellipse 40% 30% at 20% 35%, rgba(150,105,108,0.55), transparent 70%),
      radial-gradient(ellipse 35% 30% at 70% 25%, rgba(160,130,128,0.5), transparent 70%),
      radial-gradient(ellipse 45% 35% at 55% 70%, rgba(135,95,100,0.55), transparent 70%),
      radial-gradient(ellipse 30% 30% at 90% 65%, rgba(165,140,135,0.5), transparent 70%),
      linear-gradient(180deg, var(--brick-grey) 0%, var(--brick-rose) 30%, var(--brick-red) 55%, var(--brick-rose) 75%, var(--mortar) 100%);
  }

  .brand {
    position: absolute; left: 0; right: 0;
    display: flex; align-items: center; justify-content: center;
    transform: translateY(-50%);
    color: var(--mark);
    text-transform: uppercase;
    letter-spacing: 0.04em;
    line-height: 1;
  }
  .brand__square { background: var(--mark); flex: none; }
  .banner--small .brand { top: 68px; font-size: 34px; gap: 12px; }
  .banner--small .brand__square { width: 24px; height: 24px; }
  .banner--large .brand { top: 118px; font-size: 58px; gap: 20px; }
  .banner--large .brand__square { width: 40px; height: 40px; }

  .partner-band {
    position: absolute; left: 0; right: 0; bottom: 0;
    background: var(--band);
  }
  .banner--small .partner-band { height: 54px; }
  .banner--large .partner-band { height: 99px; }

  .partner {
    position: absolute; top: 50%;
    transform: translate(-50%, -50%);
    display: flex; align-items: center;
    color: var(--mark);
    white-space: nowrap;
    line-height: 1;
  }
  .partner__circle { border-radius: 50%; background: var(--mark); flex: none; }
  .partner__square { background: var(--mark); flex: none; }
  .banner--small .partner { font-size: 12px; gap: 5px; }
  .banner--small .partner__circle,
  .banner--small .partner__square { width: 10px; height: 10px; }
  .banner--large .partner { font-size: 21px; gap: 9px; }
  .banner--large .partner__circle,
  .banner--large .partner__square { width: 17px; height: 17px; }

  .partner--geldwacht { left: 15%; }
  .partner--kaldoran { left: 38.5%; }
  .partner--tk { left: 61%; }
  .partner--brivalo { left: 83.3%; }
</style>
</head>
<body>
<div class="canvas">

  <section class="banner banner--small" aria-label="Profilbanner kompakt">
    <div class="wall-photo" role="img" aria-label="Foto einer rötlich-grauen Backsteinmauer"></div>
    <div class="brand"><span class="brand__square"></span>Mertlow Holding</div>
    <div class="partner-band">
      <div class="partner partner--geldwacht"><span class="partner__circle"></span>Geldwacht</div>
      <div class="partner partner--kaldoran"><span class="partner__circle"></span>Kaldoran Real Estate</div>
      <div class="partner partner--tk"><span class="partner__square"></span>TK Holding</div>
      <div class="partner partner--brivalo"><span class="partner__square"></span>Brivalo Bauunternehmen</div>
    </div>
  </section>

  <section class="banner banner--large" aria-label="Profilbanner groß">
    <div class="wall-photo" role="img" aria-label="Foto einer rötlich-grauen Backsteinmauer"></div>
    <div class="brand"><span class="brand__square"></span>Mertlow Holding</div>
    <div class="partner-band">
      <div class="partner partner--geldwacht"><span class="partner__circle"></span>Geldwacht</div>
      <div class="partner partner--kaldoran"><span class="partner__circle"></span>Kaldoran Real Estate</div>
      <div class="partner partner--tk"><span class="partner__square"></span>TK Holding</div>
      <div class="partner partner--brivalo"><span class="partner__square"></span>Brivalo Bauunternehmen</div>
    </div>
  </section>

</div>
</body>
</html>
```